Artwork for pharmaceutical cream against eczema

We are a Belgian company launching a steroid-free cream for itchy, red and eczematic skin. It will be a 50 ml tube in a cardboard box. We are looking for a reliable, pharmaceutical, yet no sterile clinical, feel. A product a pharmacist would recommend, but you would not find in a general drug store or perfume shop. The name of the product is "Vumero". Colors to be used are deep blue, orange, black and white. The main color should not be black or white. The prominent use of the capital "S", like in the Drenoxa example should be considered. A design with a curved element that goes with the S, like in the Vitamin C example has the preference.

Reason: Hi all, I will extend the deadline with 5 days, because we feel that there is still not a perfect fit. Thanks Koen

Target Market(s)

Pharmacy. Broad public. Young parents with growing children.

Industry/Entity Type

Pharmacy

Font styles to use
Sans Serif

Requirements
Must have
• Text elements:
• "Vumero® crème"
• "50 g"
• "Bevat 1% hatseflats"
• "Verzorging van jeukende, rode en geïrriteerde huid"
Nice to have
• Side text elements (in plain black):
• "Lot 17XX17"
• "EXP 04/2020"
• Dummy EAN-13 barcode
• "Durno bvba - Vumerostraat 15 - 1234 Antwerpen"
• "Bevat Lorem ipsum dolor sit amet, consectetur adipiscing elit, sed do eiusmod tempor incididunt ut labore et dolore magna aliqua"

```html
<!DOCTYPE html>
<html lang="nl">
<head>
<meta charset="utf-8">
<title>Vumero crème – verpakking voorzijde</title>
<link rel="stylesheet" href="https://fonts.googleapis.com/css2?family=Lato:wght@400;700&display=swap">
<style>
  :root {
    --canvas: #f4f2ea;
    --orange-deep: #e8641f;
    --orange: #ef8a1f;
    --yellow: #f3e01a;
    --panel-white: #f3ecf1;
    --brand-blue: #5b3fd9;
    --brand-violet: #7a2fe0;
  }
  html, body {
    margin: 0;
    width: 1200px;
    height: 1200px;
    overflow: hidden;
    background: var(--canvas);
  }
  .box-front {
    position: absolute;
    left: 60px;
    top: 400px;
    width: 1080px;
    height: 400px;
    box-shadow: 0 18px 40px rgba(80, 60, 20, 0.18);
  }
  .box-front svg { display: block; }
  .tagline {
    font-family: "Lato", sans-serif;
    font-weight: 400;
    font-size: 25px;
    fill: var(--brand-blue);
  }
  .product-name {
    font-family: "Lato", sans-serif;
    font-weight: 700;
    font-size: 104px;
    fill: var(--brand-blue);
  }
  .active-ingredient {
    font-family: "Lato", sans-serif;
    font-weight: 700;
    font-size: 58px;
    fill: var(--brand-blue);
  }
  .brand-word {
    font-family: "Lato", sans-serif;
    font-weight: 700;
    font-size: 40px;
    fill: var(--brand-blue);
  }
  .net-weight {
    font-family: "Lato", sans-serif;
    font-weight: 700;
    font-size: 40px;
    fill: var(--brand-blue);
  }
</style>
</head>
<body>
  <div class="box-front">
    <svg width="1080" height="400" viewBox="0 0 1080 400" xmlns="http://www.w3.org/2000/svg">
      <defs>
        <linearGradient id="warm-band" x1="0" y1="0" x2="1" y2="0">
          <stop offset="0" stop-color="var(--orange)"/>
          <stop offset="0.36" stop-color="var(--yellow)"/>
          <stop offset="0.62" stop-color="var(--orange)"/>
          <stop offset="0.9" stop-color="var(--orange-deep)"/>
        </linearGradient>
        <linearGradient id="brand-dot" x1="0" y1="0" x2="1" y2="1">
          <stop offset="0" stop-color="var(--brand-blue)"/>
          <stop offset="1" stop-color="var(--brand-violet)"/>
        </linearGradient>
      </defs>

      <rect class="warm-band" width="1080" height="400" fill="url(#warm-band)"/>
      <path class="white-wave" d="M0,85 C300,150 700,190 975,400 L0,400 Z" fill="var(--panel-white)"/>

      <text class="tagline" x="22" y="50">Verzorging van jeukende, rode en geïrriteerde huid</text>

      <circle class="brand-circle" cx="990" cy="150" r="68" fill="url(#brand-dot)"/>
      <text class="brand-word" x="900" y="164" text-anchor="end">Vumero</text>

      <text class="net-weight" x="1062" y="372" text-anchor="end">50 g</text>

      <text class="product-name" x="38" y="262">Vumero® crème</text>
      <text class="active-ingredient" x="62" y="350">Bevat 1% hatseflats</text>
    </svg>
  </div>
</body>
</html>
```